Brisk Hollow Builders Needs A Flyer

We need a flyer for our newest product "The Cedarlane Garden Workroom"

Here is some copy for the flyer:

1. More and more people everyday are working from home and finding it difficult to disconnect from home activities in order to focus on their work. They are also finding it very expensive to add on to their existing house for a quiet place. Our archatectually stunning, Cedarlane Garden Workroom is the answer. The office studio measures 16' wide and 10' deep. 160 Square feet of space.

Perfect for dozens of purposes. Home office, design studio, artist studio, home school office, reading room, craft studio, drafting room.

Features include:

- Steel Framing. 40-60% lighter then wood, higher strength to weight ratio, resistant to mold and fire and steel is the most recycled material on earth!
- Spray foam insulation. Cool in the summer and warm in the winter.
- HVAC Mini Split with wireless remote control and thermostat.
- 100% Off grid with enough solar and battery storage to run your entire office. No need to pay for an expensive electric installation.
- Flush fitting floor outlets to reduce wires.
- TV mount (Optional with pre-wired electric, HDMI, digital audio & Cat 6)
- Windows are tempered glass custom made by Morvik Glazing.
- Solar qualifies for a 26% tax credit. This is not a write-off rather it is a direct reduction on your tax obligation.
- Thousands of dollars less than adding onto your home.
- Custom color, siding, features available.

This beautiful back yard office is delivered 100% assembled and ready to enjoy on the day of delivery.

We ship nationwide from our factory in South Carolina. Give us a call anytime to speak to a designer and start your dream office today!

555-318-4027
info@BriskHollowBuilders.example

```html
<!DOCTYPE html>
<html lang="en">
<head>
<meta charset="utf-8">
<title>Brisk Hollow Builders – Cedarlane Garden Workroom</title>
<link rel="stylesheet" href="https://fonts.googleapis.com/css2?family=Archivo+Black&family=Arimo:wght@400;700&display=swap">
<style>
  :root {
    --gold: #f5b01a;
    --gold-deep: #f0a81c;
    --white: #ffffff;
    --plum-dark: #2c2340;
    --plum: #3b2f52;
    --plum-light: #4a3d63;
    --band: #e3e3e8;
    --band-text: #3a3a44;
    --strip: #d9d9de;
    --sky-top: #9fb4c4;
    --sky-mid: #6b6f85;
  }
  * { box-sizing: border-box; margin: 0; padding: 0; }
  html, body { width: 927px; height: 1200px; overflow: hidden; background: var(--plum-dark); }
  .flyer {
    position: relative;
    width: 927px;
    height: 1200px;
    overflow: hidden;
    font-family: "Arimo", Arial, sans-serif;
    color: var(--white);
    background: radial-gradient(ellipse at 50% 78%, var(--plum-light) 0%, var(--plum) 45%, var(--plum-dark) 100%);
  }
  .hero-photo {
    position: absolute; left: 0; top: 0; width: 927px; height: 496px;
    background:
      linear-gradient(180deg, rgba(44,35,64,0) 55%, rgba(44,35,64,0.85) 100%),
      linear-gradient(180deg, var(--sky-top) 0%, var(--sky-mid) 30%, #4b4460 60%, #3a3049 100%);
  }
  .brand {
    position: absolute; left: 22px; top: 62px; width: 160px;
    font-weight: 700; font-size: 19px; line-height: 1.05; color: var(--gold-deep);
    text-align: center; text-transform: uppercase;
  }
  .headline { position: absolute; left: 0; width: 927px; text-align: center; text-transform: uppercase; }
  .headline-main {
    top: 339px; font-family: "Archivo Black", sans-serif; font-size: 51px;
    color: var(--gold); letter-spacing: 0.5px; line-height: 1;
  }
  .headline-sub {
    top: 394px; font-family: "Archivo Black", sans-serif; font-size: 27px;
    color: var(--white); line-height: 1;
  }
  .headline-lines {
    top: 423px; font-weight: 700; font-size: 23.5px; color: var(--gold); line-height: 27px;
  }
  .intro-band {
    position: absolute; left: 0; top: 496px; width: 927px; height: 65px;
    background: var(--band); color: var(--band-text);
    padding: 8px 60px 0 68px; font-size: 12.8px; line-height: 17px;
  }
  .features {
    position: absolute; left: 39px; top: 579px; width: 842px; height: 288px;
    border: 2px dashed var(--white); border-radius: 20px;
  }
  .features-title {
    position: absolute; left: 84px; top: -15px; padding: 0 9px;
    background: var(--plum); font-family: "Archivo Black", sans-serif;
    font-size: 20px; color: var(--gold); line-height: 26px;
  }
  .feature-list {
    position: absolute; left: 13px; top: 25px;
    list-style: none; font-weight: 700; font-size: 14px; line-height: 16.8px;
  }
  .feature-list.top li { width: 474px; text-align: justify; }
  .feature-list.bottom { top: 172px; }
  .feature-list.bottom li { white-space: nowrap; }
  .product-photo {
    position: absolute; left: 499px; top: 23px; width: 324px; height: 139px;
    background: linear-gradient(180deg, #8aa0a8 0%, #6f7f76 45%, #4d5a45 75%, #3d4735 100%);
  }
  .delivery { position: absolute; left: 0; width: 927px; text-align: center; text-transform: uppercase; }
  .delivery-lead { top: 903px; font-weight: 700; font-size: 15.5px; }
  .delivery-big { top: 930px; font-family: "Archivo Black", sans-serif; font-size: 38px; color: var(--gold); line-height: 1; }
  .delivery-tail { top: 966px; font-family: "Archivo Black", sans-serif; font-size: 13.5px; color: var(--gold); }
  .shipping { top: 1022px; font-weight: 700; font-size: 15px; line-height: 20px; }
  .contact { position: absolute; right: 84px; top: 1111px; text-align: right; }
  .contact-phone {
    display: flex; align-items: center; justify-content: flex-end; gap: 7px;
    font-weight: 700; font-size: 17px;
  }
  .contact-email { font-weight: 700; font-size: 10px; margin-top: 5px; letter-spacing: 0.2px; }
  .brand-small {
    position: absolute; left: 840px; top: 1111px; width: 60px;
    font-weight: 700; font-size: 8px; line-height: 1.1; color: var(--gold-deep);
    text-transform: uppercase; text-align: center;
  }
  .footer-strip { position: absolute; left: 0; top: 1160px; width: 927px; height: 9px; background: var(--strip); }
  .footer-base { position: absolute; left: 0; top: 1169px; width: 927px; height: 31px; background: var(--plum-dark); }
</style>
</head>
<body>
<main class="flyer">
  <div class="hero-photo" role="img" aria-label="Dusk view of a dark-sided garden office with a slanted roof and tall glass windows among trees"></div>
  <div class="brand">Brisk Hollow Builders</div>

  <h1 class="headline headline-main">More and More!</h1>
  <p class="headline headline-sub">People everyday are working</p>
  <p class="headline headline-lines">From home and finding it difficult to disconnect<br>from home activities in order to focus on their work</p>

  <section class="intro-band">
    <p>They are also finding it very expensive to add on to their existing house for a quiet place. Our archatectually stunning, Cedarlane Garden Workroom is the answer. The office studio measures 16' wide and 10' deep. 160 Square feet of space.</p>
    <p>Perfect for dozens of purposes. Home office, design studio, artist studio, home school office, reading room, craft studio, drafting room.</p>
  </section>

  <section class="features">
    <h2 class="features-title">Features include</h2>
    <ul class="feature-list top">
      <li>- Steel Framing. 40-60% lighter then wood, higher strength to weight ratio, resistant to mold and fire and steel is the most recycled material on earth!</li>
      <li>- Spray foam insulation. Cool in the summer and warm in the winter.</li>
      <li>- HVAC Mini Split with wireless remote control and thermostat.</li>
      <li>- 100% Off grid with enough solar and battery storage to run your entire office. No need to pay for an expensive electric installation.</li>
    </ul>
    <div class="product-photo" role="img" aria-label="Side view of the garden workroom with solar panels on its sloped roof, set on a lawn with plantings"></div>
    <ul class="feature-list bottom">
      <li>- Flush fitting floor outlets to reduce wires.</li>
      <li>- TV mount (Optional with pre-wired electric, HDMI, digital audio &amp; Cat 6)</li>
      <li>- Windows are tempered glass custom made by Morvik Glazing.</li>
      <li>- Solar qualifies for a 26% tax credit. This is not a write-off rather it is a direct reduction on your tax obligation.</li>
      <li>- Thousands of dollars less than adding onto your home.</li>
      <li>- Custom color, siding, features available.</li>
    </ul>
  </section>

  <p class="delivery delivery-lead">This beautiful back yard office is delivered</p>
  <p class="delivery delivery-big">100% Assembled</p>
  <p class="delivery delivery-tail">And ready to enjoy on the day of delivery</p>
  <p class="delivery shipping">We ship nationwide from our factory in South Carolina.<br>Give us a call anytime to speak to a designer and start your dream office today!</p>

  <div class="contact">
    <div class="contact-phone">
      <svg width="16" height="16" viewBox="0 0 16 16" aria-hidden="true">
        <rect width="16" height="16" rx="3" fill="#f0a81c"/>
        <path d="M5 3.5c.5 0 1.3 1.6 1.3 2.1S5.6 6.4 5.6 7c.5 1.3 1.9 2.8 3.3 3.3.5 0 .9-.8 1.4-.8s2.1.8 2.1 1.3c0 .9-1 1.7-1.9 1.7-3.6-.4-6.3-3.2-6.7-6.7C3.8 4.6 4.2 3.5 5 3.5z" fill="#ffffff"/>
      </svg>
      <span>555-318-4027</span>
    </div>
    <div class="contact-email">INFO@BRISKHOLLOWBUILDERS.EXAMPLE</div>
  </div>
  <div class="brand-small">Brisk Hollow Builders</div>

  <div class="footer-strip"></div>
  <div class="footer-base"></div>
</main>
</body>
</html>
```